Broschüren-Design für Schuhmanufaktur
Zielgruppe
Schuhmanufaktur für Maßschuhe möchte sich modernisieren.
Aufgabenstellung
Maße und andere Daten entnehmen Sie sich den angefügten Daten und Bildern.
Es soll eine Broschüre (Maße etc in daten und skizze) und ein Plakat mit composing erstellt werden.
Offene Daten erwünscht (.ai)

```html
<!DOCTYPE html>
<html lang="de">
<head>
<meta charset="utf-8">
<title>Schuhmanufaktur Schrittwerk – Marken-Styleguide</title>
<link href="https://fonts.googleapis.com/css2?family=Quicksand:wght@300;400;600;700&family=Lato:wght@300;400;700&display=swap" rel="stylesheet">
<style>
  :root{
    --grau:#363533;
    --dunkelbraun:#2c1e1a;
    --hellbraun:#a75716;
    --beige:#c18235;
    --papier:#f5f4f2;
    --buehne:#e6e5e3;
    --text:#2a2a2a;
    --text-leise:#777;
  }
  *{box-sizing:border-box;margin:0;padding:0}
  html,body{width:800px;height:1200px;overflow:hidden}
  body{background:var(--buehne);font-family:"Lato",sans-serif;color:var(--text);position:relative}

  /* Titelseite */
  .cover{position:absolute;left:20px;top:20px;width:760px;height:540px;display:flex;background:#fff}
  .cover-photo{width:50%;height:100%;background:linear-gradient(160deg,#c9a66a 0%,#a9a39a 30%,#2f3b55 50%,#4a2d22 72%,#9c948a 100%)}
  .cover-panel{width:50%;height:100%;display:flex;flex-direction:column;align-items:center;padding-top:60px;font-family:"Quicksand",sans-serif}
  .brand-mark{display:flex;align-items:center;gap:10px;font-family:"Quicksand",sans-serif;font-weight:700;color:#111}
  .brand-mark .dot{border-radius:50%;background:#111}
  .cover .brand-mark{font-size:30px}
  .cover .brand-mark .dot{width:34px;height:34px}
  .cover-kicker{margin-top:80px;font-size:32px;font-weight:400;color:#222}
  .cover-title{font-size:54px;font-weight:700;color:#222;line-height:1.05}
  .cover-label{margin-top:auto;margin-bottom:52px;background:var(--hellbraun);color:#fff;font-size:22px;padding:6px 12px}

  /* Doppelseiten */
  .spread{position:absolute;width:370px;height:128px;display:flex;box-shadow:0 1px 3px rgba(0,0,0,.12)}
  .page{position:relative;width:50%;height:100%;overflow:hidden}
  .page-right{background:var(--papier);padding:9px 10px}
  .page-left{display:flex}
  .section-band{width:40%;background:var(--dunkelbraun);position:relative}
  .section-band .brand-mark{position:absolute;left:7px;top:8px;font-size:6px;color:#fff;gap:3px}
  .section-band .brand-mark .dot{width:6px;height:6px;background:#fff}
  .section-name{position:absolute;left:7px;top:58px;font-family:"Quicksand",sans-serif;font-weight:700;font-size:7px;letter-spacing:.6px;color:#fff;line-height:1.3}
  .section-photo{flex:1}
  .folio{position:absolute;bottom:3px;font-family:"Quicksand",sans-serif;font-weight:700;font-size:7px}
  .page-left .folio{left:5px;color:#fff}
  .page-right .folio{right:5px;color:var(--text)}
  .tag{display:inline-block;background:var(--beige);color:#fff;font-family:"Quicksand",sans-serif;font-weight:700;font-size:7px;padding:1px 3px;margin-bottom:3px}
  .tag.dark{background:var(--hellbraun)}
  .body-copy{font-size:3.6px;line-height:1.45;color:#555}

  .toc{list-style:none;margin-top:6px;width:75px}
  .toc li{display:flex;justify-content:space-between;font-size:4.2px;color:#666;padding:3px 0}
  .toc li span:last-child{color:var(--hellbraun);font-weight:700}

  .bullets{list-style:none;margin-top:3px}
  .bullets li{font-size:3.6px;color:var(--hellbraun);line-height:1.5}
  .bullets b{color:var(--dunkelbraun)}

  .logo-demos{display:flex;gap:14px;margin-top:4px}
  .logo-demo{width:48px;height:40px;display:flex;align-items:center;justify-content:center;box-shadow:0 0 2px rgba(0,0,0,.2)}
  .logo-demo .brand-mark{font-size:6px;gap:3px}
  .logo-demo .brand-mark .dot{width:6px;height:6px}
  .logo-demo.on-light{background:#fff}
  .logo-demo.on-dark{background:var(--grau)}
  .logo-demo.on-dark .brand-mark{color:#fff}
  .logo-demo.on-dark .dot{background:#fff}
  .demo-note{font-size:3.4px;color:#777;width:48px;margin-top:3px}

  .swatches{display:flex;gap:8px;margin:2px 0 6px}
  .swatch{width:56px;height:20px;padding:2px 3px;color:#fff;font-size:3.2px;line-height:1.3;box-shadow:1px 1px 2px rgba(0,0,0,.25)}
  .swatch b{display:block;font-size:3.4px}

  .type-grid{display:grid;grid-template-columns:1fr 1fr;gap:2px 10px;margin-bottom:4px}
  .type-sample{font-family:"Quicksand",sans-serif;font-size:7px;line-height:1.1}
  .type-sample small{display:block;font-size:4px}
  .type-lato{font-family:"Lato",sans-serif;font-size:5px}
  .type-lato small{font-size:3.6px;display:block}

  .mood-grid{display:grid;grid-template-columns:1fr 1fr;grid-template-rows:1fr 1fr;gap:3px;height:100%}
  .mood-cell{position:relative}
  .mood-cell.poster{background:linear-gradient(160deg,#b99e78,#3d3632);padding:3px;font-family:"Quicksand",sans-serif;color:#fff;font-size:5px;font-weight:700}
  .mood-cell.info{background:var(--grau);color:#ddd;font-size:3px;padding:4px;line-height:1.5}
  .mood-cell.shoes{background:linear-gradient(135deg,#8a5a33,#3b4050 55%,#a0764c)}
  .mood-cell.layout{background:linear-gradient(135deg,#4a4644,#7a5a40 60%,#2f2d2c)}

  .back-page{background:#2f2e2d;color:#cfcfcf;display:flex;flex-direction:column;justify-content:center;padding-left:40px;font-size:4px;line-height:1.6}
  .back-page strong{font-size:4.4px;color:#eee}
  .mini-cover{display:flex;padding:0}
  .mini-cover .mini-photo{width:50%;background:linear-gradient(160deg,#c9a66a,#2f3b55 50%,#4a2d22 75%,#9c948a)}
  .mini-cover .mini-panel{width:50%;background:#fff;display:flex;flex-direction:column;align-items:center;padding-top:14px;font-family:"Quicksand",sans-serif}
  .mini-panel .brand-mark{font-size:6px;gap:3px}
  .mini-panel .brand-mark .dot{width:6px;height:6px}
  .mini-panel .k{margin-top:16px;font-size:6px}
  .mini-panel .t{font-size:10px;font-weight:700}
  .mini-panel .l{margin-top:auto;margin-bottom:10px;background:var(--hellbraun);color:#fff;font-size:4.5px;padding:1px 3px}
</style>
</head>
<body>

<section class="cover">
  <div class="cover-photo" role="img" aria-label="Foto: Bein in Nadelstreifenhose mit dunkelbraunem Budapester und Lederkoffer auf herbstlicher Steintreppe"></div>
  <div class="cover-panel">
    <div class="brand-mark"><span class="dot"></span>Schrittwerk</div>
    <p class="cover-kicker">Schuhmanufaktur</p>
    <h1 class="cover-title">Schrittwerk</h1>
    <p class="cover-label">Marken-Styleguide</p>
  </div>
</section>

<!-- Inhalt -->
<article class="spread" style="left:20px;top:590px">
  <div class="page" style="background:var(--grau);display:flex;align-items:center;justify-content:center">
    <div class="brand-mark" style="color:#fff;font-size:9px;gap:4px"><span class="dot" style="width:9px;height:9px;background:#fff"></span>Schrittwerk</div>
  </div>
  <div class="page page-right">
    <span class="tag dark">Marken Style-Guide</span>
    <ul class="toc">
      <li><span>Marken-Philosophie</span><span>04</span></li>
      <li><span>Logo</span><span>06</span></li>
      <li><span>Farbpalette</span><span>08</span></li>
      <li><span>Typographie</span><span>10</span></li>
      <li><span>Moodboard</span><span>12</span></li>
    </ul>
  </div>
</article>

<!-- Marken-Philosophie -->
<article class="spread" style="left:410px;top:590px">
  <div class="page page-left">
    <div class="section-band">
      <div class="brand-mark"><span class="dot"></span>Schrittwerk</div>
      <p class="section-name">MARKEN-<br>PHILOSOPHIE</p>
    </div>
    <div class="section-photo" role="img" aria-label="Foto: zwei cognacfarbene Budapester mit Ledergürtel auf Holzboden" style="background:linear-gradient(135deg,#3a2a1e,#c0802e 45%,#e1a045 60%,#4a3422)"></div>
    <span class="folio">4</span>
  </div>
  <div class="page page-right">
    <span class="tag">Schuhmanufaktur</span><br>
    <span class="tag">Schrittwerk</span>
    <p class="body-copy">Im September 2001 eröffneten wir Geschwister, Lena Ortolani und Marco Venzi, unsere Schuhmanufaktur. Zuvor hatten wir beide den Meisterbrief erworben und mehrere Jahre in verschiedenen Werkstätten Berufserfahrung gesammelt. Im September 2021 feiern wir also das 20-jährige Bestehen unserer Manufaktur.</p>
    <p class="body-copy" style="font-weight:700;color:#333;margin-top:3px">Leder ist unsere Leidenschaft</p>
    <ul class="bullets">
      <li>• <b>Reparatur:</b> Wir ermöglichen hochwertigen Lederwaren lange Nutzbarkeit</li>
      <li>• <b>Optimierung:</b> Wir übernehmen spezielle Anpassungswünsche</li>
      <li>• <b>Kreation:</b> Wir fertigen individuelle Maßschuhe</li>
    </ul>
    <span class="folio">5</span>
  </div>
</article>

<!-- Logo -->
<article class="spread" style="left:20px;top:732px">
  <div class="page page-left">
    <div class="section-band">
      <div class="brand-mark"><span class="dot"></span>Schrittwerk</div>
      <p class="section-name">LOGO</p>
    </div>
    <div class="section-photo" role="img" aria-label="Foto: hellbraune Oxford-Schuhe auf grauem Tweedstoff" style="background:linear-gradient(135deg,#6b7078,#b0643a 45%,#d88a4e 60%,#5a5e66)"></div>
    <span class="folio">6</span>
  </div>
  <div class="page page-right">
    <span class="tag">Anwendung des Logos</span>
    <div class="logo-demos">
      <div>
        <div class="logo-demo on-light"><div class="brand-mark"><span class="dot"></span>Schrittwerk</div></div>
        <p class="demo-note">Logo in 0/0/0/100 Schwarz auf hellem Hintergrund.</p>
      </div>
      <div>
        <div class="logo-demo on-dark"><div class="brand-mark"><span class="dot"></span>Schrittwerk</div></div>
        <p class="demo-note">Logo in 0/0/0/0 Weiß auf dunklem Hintergrund.</p>
      </div>
    </div>
    <span class="folio">7</span>
  </div>
</article>

<!-- Farbpalette -->
<article class="spread" style="left:410px;top:732px">
  <div class="page page-left">
    <div class="section-band">
      <div class="brand-mark"><span class="dot"></span>Schrittwerk</div>
      <p class="section-name">FARBPALETTE</p>
    </div>
    <div class="section-photo" role="img" aria-label="Foto: Wildleder-Loafer mit Quasten auf dunklem Holzboden" style="background:linear-gradient(160deg,#0f2224,#5f6c68 45%,#a98a62 60%,#3a4a4a)"></div>
    <span class="folio">8</span>
  </div>
  <div class="page page-right">
    <span class="tag">Primärfarben</span>
    <div class="swatches">
      <div class="swatch" style="background:var(--grau)"><b>GRAU</b>CMYK 67/58/57/65<br>RGB 55/54/52<br>#363533</div>
      <div class="swatch" style="background:var(--dunkelbraun)"><b>DUNKELBRAUN</b>CMYK 56/66/61/82<br>RGB 45/30/26<br>#2c1e1a</div>
    </div>
    <span class="tag dark">Sekundärfarben</span>
    <div class="swatches">
      <div class="swatch" style="background:var(--hellbraun)"><b>HELLBRAUN</b>CMYK 26/68/100/19<br>RGB 168/87/23<br>#a75716</div>
      <div class="swatch" style="background:var(--beige)"><b>BEIGE</b>CMYK 23/49/86/15<br>RGB 193/131/53<br>#c18235</div>
    </div>
    <span class="folio">9</span>
  </div>
</article>

<!-- Typographie -->
<article class="spread" style="left:20px;top:874px">
  <div class="page page-left">
    <div class="section-band">
      <div class="brand-mark"><span class="dot"></span>Schrittwerk</div>
      <p class="section-name">TYPOGRAPHIE</p>
    </div>
    <div class="section-photo" role="img" aria-label="Foto: cognacfarbener Oxford-Schuh auf Holzdielen" style="background:linear-gradient(150deg,#2a1a12,#b8672a 45%,#d9853c 58%,#3a2418)"></div>
    <span class="folio">10</span>
  </div>
  <div class="page page-right">
    <span class="tag">Überschriften</span>
    <div class="type-grid">
      <p class="type-sample" style="font-weight:700">Quicksand<small>Bold</small></p>
      <p class="type-sample" style="font-weight:400">Quicksand<small>Regular</small></p>
    </div>
    <span class="tag dark">Textkörper</span>
    <div class="type-grid">
      <p class="type-lato" style="font-weight:300">Lato<small>Light</small></p>
      <p class="type-lato" style="font-weight:700">Lato<small>Bold</small></p>
      <p class="body-copy" style="font-weight:300">Daepta di dolorrum ut hil event milliquodit accum, alicili catur? Od mi, ut fugit pos derernam, tem is aut.</p>
      <p class="body-copy" style="font-weight:700;color:#222">Daepta di dolorrum ut hil event milliquodit accum, alicili catur? Od mi, ut fugit pos derernam, tem is aut.</p>
    </div>
    <span class="folio">11</span>
  </div>
</article>

<!-- Moodboard -->
<article class="spread" style="left:410px;top:874px">
  <div class="page page-left">
    <div class="section-band">
      <div class="brand-mark"><span class="dot"></span>Schrittwerk</div>
      <p class="section-name">MOODBOARD</p>
    </div>
    <div class="section-photo" role="img" aria-label="Foto: dunkelbraune Chelsea-Boots vor dunklem Hintergrund" style="background:linear-gradient(150deg,#1e1e1e,#6a3a26 50%,#9a5a3c 62%,#cfcfcf)"></div>
    <span class="folio">12</span>
  </div>
  <div class="page page-right" style="padding:6px 14px 12px 8px">
    <div class="mood-grid">
      <div class="mood-cell poster" role="img" aria-label="Plakat-Entwurf mit Schuhfoto">Schuhmanufaktur<br>Schrittwerk</div>
      <div class="mood-cell info">Schuhmanufaktur Schrittwerk GmbH<br>Lederweg 12, Leipzig<br>Maßschuhe seit 2001<br>Termine nach Vereinbarung</div>
      <div class="mood-cell shoes" role="img" aria-label="Collage klassischer Herrenschuhe"></div>
      <div class="mood-cell layout" role="img" aria-label="Broschürenseiten mit Schuhfotos"></div>
    </div>
    <span class="folio">13</span>
  </div>
</article>

<!-- Rückseite und Titel -->
<article class="spread" style="left:215px;top:1016px">
  <div class="page back-page">
    <strong>Schuhmanufaktur Schrittwerk GmbH</strong>
    <span>Lederweg 12 · 04109 Leipzig</span>
    <span>Tel. 0341 555 0192</span>
    <span>info@schuhmanufaktur-schrittwerk.de</span>
    <span style="margin-top:3px">www.schuhmanufaktur-schrittwerk.de</span>
  </div>
  <div class="page mini-cover">
    <div class="mini-photo" role="img" aria-label="Foto: Budapester auf herbstlicher Treppe"></div>
    <div class="mini-panel">
      <div class="brand-mark"><span class="dot"></span>Schrittwerk</div>
      <p class="k">Schuhmanufaktur</p>
      <p class="t">Schrittwerk</p>
      <p class="l">Marken-Styleguide</p>
    </div>
  </div>
</article>

</body>
</html>
```